Medical Oncologist in Rural Australia needs a Business Card

I am a medical oncologist in a regional town in Australia. I need a business card that merges a degree of conservatism (as people's lives are entrusted to me) with cutting edge (as I am always trying to understand the latest cancer biology and trying to bring new drugs to patients rapidly). I wish my card to project the idea that I am trustworthy, caring and innovative. Not overly bold colours but something that doesn't drift into the background.

Medical

```html
<!DOCTYPE html>
<html lang="en">
<head>
<meta charset="utf-8">
<title>Medical Oncologist – Business Card</title>
<link rel="stylesheet" href="https://fonts.googleapis.com/css2?family=Exo+2:wght@400;500;700;800&family=Kaushan+Script&display=swap">
<style>
  :root {
    --page-bg: #e9eaec;
    --card-white: #f4f4f4;
    --card-shade: #e2e2e3;
    --ink: #1c1c1e;
    --brand-blue: #4b77c8;
    --brand-blue-deep: #3f67b4;
    --soft-white: #f7f7f7;
  }
  * { box-sizing: border-box; margin: 0; padding: 0; }
  html, body { width: 1200px; height: 873px; overflow: hidden; }
  body {
    background: var(--page-bg);
    font-family: "Exo 2", sans-serif;
    display: flex;
    align-items: center;
    justify-content: center;
    gap: 60px;
  }
  .card {
    position: relative;
    width: 520px;
    height: 300px;
    border-radius: 4px;
    overflow: hidden;
    box-shadow: 0 10px 28px rgba(0,0,0,.18);
  }

  /* front */
  .card-front {
    background: linear-gradient(135deg, var(--card-white) 0%, #ffffff 55%, var(--card-shade) 100%);
    padding: 26px 30px;
    color: var(--ink);
  }
  .contact-list { list-style: none; display: flex; flex-direction: column; gap: 3px; }
  .contact-item {
    display: flex; align-items: center; gap: 10px;
    font-size: 17px; font-weight: 400; color: var(--brand-blue);
    letter-spacing: .5px;
  }
  .contact-icon { width: 18px; height: 18px; flex: none; fill: var(--ink); }
  .specialty-title { margin-top: 22px; line-height: .92; font-weight: 800; letter-spacing: -.5px; }
  .specialty-title .line-medical { display: block; font-size: 34px; color: var(--ink); }
  .specialty-title .line-oncologist { display: block; font-size: 36px; color: var(--brand-blue); }
  .doctor-name {
    position: absolute; right: 30px; bottom: 48px;
    font-size: 40px; font-weight: 700; color: var(--ink); letter-spacing: .5px;
  }
  .doctor-name .title-prefix {
    font-family: "Kaushan Script", cursive; font-weight: 400;
    color: var(--brand-blue); font-size: 36px; margin-right: 12px;
  }
  .credentials {
    position: absolute; right: 30px; bottom: 28px;
    font-size: 12.5px; color: var(--ink);
  }

  /* back */
  .card-back { background: var(--brand-blue); }
  .card-back .wave { position: absolute; inset: 0; width: 100%; height: 100%; }
  .back-title {
    position: absolute; left: 48px; top: 92px;
    font-weight: 800; line-height: .9; letter-spacing: -.5px;
  }
  .back-title .line-medical { display: block; font-size: 46px; color: var(--ink); }
  .back-title .line-oncologist { display: block; font-size: 52px; color: var(--soft-white); }
  .tagline {
    position: absolute; left: 52px; top: 200px;
    font-family: "Kaushan Script", cursive; font-size: 22px; color: #1d2a44;
  }
</style>
</head>
<body>
  <section class="card card-front" aria-label="Business card front">
    <ul class="contact-list">
      <li class="contact-item">
        <svg class="contact-icon" viewBox="0 0 24 24" aria-hidden="true"><path d="M7 2h10a2 2 0 0 1 2 2v16a2 2 0 0 1-2 2H7a2 2 0 0 1-2-2V4a2 2 0 0 1 2-2zm0 3v13h10V5H7zm5 14.2a1 1 0 1 0 0 2 1 1 0 0 0 0-2z"/></svg>
        0 123 456 89
      </li>
      <li class="contact-item">
        <svg class="contact-icon" viewBox="0 0 24 24" aria-hidden="true"><path d="M3 9c0-3 4-5 9-5s9 2 9 5l-3 2-2-2V7H8v2l-2 2-3-2zm4 4h10l3 7H4l3-7zm5 1.5a2.5 2.5 0 1 0 0 5 2.5 2.5 0 0 0 0-5z"/></svg>
        0 123 456 78
      </li>
      <li class="contact-item">
        <svg class="contact-icon" viewBox="0 0 24 24" aria-hidden="true"><path d="M12 2a10 10 0 1 0 5 18.7l-1-1.7A8 8 0 1 1 20 12v1a2 2 0 0 1-4 0V7h-2v1a5 5 0 1 0 .9 7.1A4 4 0 0 0 22 13v-1A10 10 0 0 0 12 2zm0 7a3 3 0 1 1 0 6 3 3 0 0 1 0-6z"/></svg>
        yourname@website.com
      </li>
    </ul>
    <h1 class="specialty-title">
      <span class="line-medical">medical</span>
      <span class="line-oncologist">oncologist</span>
    </h1>
    <p class="doctor-name"><span class="title-prefix">dr.</span>Your Name</p>
    <p class="credentials">specialized in MBBS (hons), FRACP BE (hons)</p>
  </section>

  <section class="card card-back" aria-label="Business card back">
    <svg class="wave" viewBox="0 0 520 300" preserveAspectRatio="none" aria-hidden="true">
      <defs>
        <linearGradient id="wave-fill" x1="0" y1="0" x2="1" y2="1">
          <stop offset="0" stop-color="#ffffff"/>
          <stop offset="1" stop-color="#dcdcde"/>
        </linearGradient>
      </defs>
      <path d="M520 0 H300 C360 60 420 80 430 150 C440 220 400 260 430 300 H520 Z" fill="url(#wave-fill)"/>
    </svg>
    <h2 class="back-title">
      <span class="line-medical">medical</span>
      <span class="line-oncologist">oncologist</span>
    </h2>
    <p class="tagline">your quote here</p>
  </section>
</body>
</html>
```